Health and Wellness Company Business Card

I need a business card design that is clean and uses modern minimalist style. The design should incorporate our logo (see attached). I would also like to use embossing on the cards so that they also have a great feel. I am open to the card using one or more colors, and these do not have to correspond to the colors in the concept paper. The card can either be one-sided or use both sides of the card.The logo uses the Avenir font.

I will need the file designed in Adobe CS and compatible with CS5.5 (Illustrator preferable) and I'll need the working file (for example: .ai) once the project is complete so that I can change the names/contact info/etc for each variation of the card.

This needs to be a memorable card for the recipient. They should think: "This is a great business card" either because of its simplicity or embossing effects or use of color.

Target Market(s)

The audience for our company has two main groups: people who pay for healthcare (insurers, companies, researcher companies) and people with chronic health conditions who are the consumers of our services and resources.

Industry/Entity Type

Business

Requirements
Must have
• Essential components of the card include: Company logo, contact Name (Mark Tolley), phone number (5808127346), email address (mtolley@brenquora.com), slogan/tagline that consists of ~30-40 characters (Use Lorem Ipsum)
Nice to have
• These fall just slightly short of "must have" to allow for design flexibility: Embossing or spot varnish effects and a splash of color
Should not have
• Designs with these components will not be successful: flashy or showy designs that are not professional in appearance, and lots of different colors

```html
<!DOCTYPE html>
<html lang="en">
<head>
<meta charset="utf-8">
<title>Brenquora Business Card</title>
<link href="https://fonts.googleapis.com/css2?family=Nunito+Sans:wght@400;700&display=swap" rel="stylesheet">
<style>
  :root {
    --backdrop: #3a302b;
    --card-white: #f7f7f6;
    --card-black: #141414;
    --ink-grey: #6d6b72;
    --ink-dark: #57555c;
    --ink-soft: #8f8d93;
    --gloss-grey: #8a8a8a;
    --gloss-dim: #5e5e5e;
  }
  * { margin: 0; padding: 0; box-sizing: border-box; }
  html, body {
    width: 1200px;
    height: 835px;
    overflow: hidden;
    background: var(--backdrop);
    font-family: "Nunito Sans", "Avenir", sans-serif;
  }
  .canvas {
    position: relative;
    width: 1200px;
    height: 835px;
  }
  .card {
    position: absolute;
    top: 258px;
    width: 520px;
    height: 318px;
    border-radius: 4px;
    box-shadow: 0 6px 18px rgba(0,0,0,0.35);
  }
  .card-front {
    left: 50px;
    background: var(--card-white);
  }
  .card-back {
    left: 630px;
    background: var(--card-black);
  }
  .brand-block {
    position: absolute;
    right: 40px;
    top: 60px;
    display: flex;
    flex-direction: column;
    align-items: flex-end;
  }
  .brand-lockup {
    display: flex;
    align-items: center;
    gap: 12px;
  }
  .brand-mark {
    width: 16px;
    height: 16px;
    background: var(--ink-grey);
    border-radius: 3px;
  }
  .brand-name {
    font-size: 21px;
    font-weight: 400;
    letter-spacing: 0.42em;
    margin-right: -0.42em;
    color: var(--ink-grey);
    text-transform: uppercase;
  }
  .brand-tagline {
    margin-top: 10px;
    font-size: 11.5px;
    font-weight: 400;
    letter-spacing: 0.04em;
    color: var(--ink-soft);
  }
  .contact {
    position: absolute;
    left: 40px;
    top: 170px;
    color: var(--ink-grey);
  }
  .contact-name {
    font-size: 15px;
    font-weight: 700;
    letter-spacing: 0.02em;
    text-transform: uppercase;
    margin-bottom: 10px;
  }
  .contact-line {
    font-size: 12.5px;
    line-height: 1.55;
  }
  .contact-label {
    font-weight: 700;
    color: var(--ink-dark);
  }
  .back-lockup {
    position: absolute;
    inset: 0;
    display: flex;
    flex-direction: column;
    align-items: center;
    justify-content: center;
  }
  .back-mark {
    width: 70px;
    height: 70px;
    background: var(--gloss-grey);
    border-radius: 12px;
    margin-bottom: 26px;
  }
  .back-name {
    font-size: 30px;
    font-weight: 400;
    letter-spacing: 0.42em;
    color: var(--gloss-grey);
    text-transform: uppercase;
    padding-left: 0.42em;
  }
  .back-tagline {
    margin-top: 14px;
    font-size: 13px;
    letter-spacing: 0.06em;
    color: var(--gloss-dim);
  }
</style>
</head>
<body>
<main class="canvas">
  <section class="card card-front" aria-label="Card front">
    <div class="brand-block">
      <div class="brand-lockup">
        <span class="brand-mark"></span>
        <span class="brand-name">Brenquora</span>
      </div>
      <p class="brand-tagline">Lorem ipsum dolor sit amet consectetur</p>
    </div>
    <div class="contact">
      <p class="contact-name">Mark Tolley</p>
      <p class="contact-line"><span class="contact-label">Mobile:</span> 580 812 7346</p>
      <p class="contact-line"><span class="contact-label">Email:</span> mtolley@brenquora.com</p>
    </div>
  </section>
  <section class="card card-back" aria-label="Card back">
    <div class="back-lockup">
      <span class="back-mark"></span>
      <span class="back-name">Brenquora</span>
      <p class="back-tagline">Lorem ipsum dolor sit amet consectetur</p>
    </div>
  </section>
</main>
</body>
</html>
```